rvtd Marketing Brochure for construction of multi-million dollar homes in the Caribbean

Design a marketing brochure for a construction company operating in the Caribbean for ultra high-end signature homes and villas. Target audience is ultra high net worth individuals, families, international property developers and hotel chains. We have provided an our marketing brochure for reference but would like a totally new look and feel with updated wording and photos (also provided). The company logo of light and dark blue circles and 'rvtd' with the 's' in superscript must feature throughout. Further information can be extracted from the company's website: rvtdharbourline.com. Depending on how this goes there may be additional projects such as website and log redesign. Thanks!

Target Market(s)

Target audience is ultra high net worth individuals, families, international property developers and hotel chains.

Font styles to use
Other font styles liked:
• see logo for desired phones

Colors
3aa7d7
0655a3
85cae6
3176b5
85acd3
33a6d7
cee9f5
cedeed

Requirements
Must have
• Detailed company info including projects and employee profiles - must be bold, brilliant and eye-catching.
Nice to have
• Colour
Should not have
• Too much info.

```html
<!DOCTYPE html>
<html lang="en">
<head>
<meta charset="utf-8">
<title>rvtd Brochure Pages</title>
<link href="https://fonts.googleapis.com/css2?family=Montserrat:wght@800&family=Open+Sans:wght@400;600&family=Roboto+Condensed:wght@300;400&display=swap" rel="stylesheet">
<style>
  :root{
    --bg:#c9dbdf;
    --paper:#ffffff;
    --ink:#3a3a3a;
    --navy:#1f4fa0;
    --deep:#0655a3;
    --indigo:#3a3f9e;
    --sky:#3aa7d7;
    --aqua:#5bbcd6;
    --pale:#cee9f5;
    --mist:#cedeed;
    --sea:#1d6fb8;
  }
  *{margin:0;padding:0;box-sizing:border-box}
  html,body{width:1200px;height:1200px;overflow:hidden;background:var(--bg)}
  body{position:relative;font-family:"Open Sans",sans-serif;color:var(--ink)}
  .page{position:absolute;width:341px;height:242px;background:var(--paper);overflow:hidden;box-shadow:3px 4px 6px rgba(0,0,0,.28)}
  .photo{position:absolute}
  .brand{position:absolute;display:flex;align-items:center;gap:4px;font-family:"Open Sans",sans-serif;font-weight:400;color:var(--navy);line-height:1}
  .brand .dot{width:9px;height:9px;border-radius:50%;background:var(--sky)}
  .brand .name{font-size:15px}
  .brand .tag{font-size:3.5px;color:#888;margin-left:4px;white-space:nowrap}
  .brand.light{color:#fff}
  .brand.light .dot{background:#fff}
  .heading{position:absolute;font-family:"Roboto Condensed",sans-serif;font-weight:400;font-size:12px;color:var(--navy);text-transform:uppercase;line-height:1;white-space:nowrap}
  .heading.aqua{color:var(--aqua);font-weight:300}
  .heading.white{color:#fff;font-weight:300}
  .copy{position:absolute;font-size:3.9px;line-height:1.45;color:var(--ink)}
  .copy.white{color:#fff}
  .copy.just{text-align:justify}
  .folio{position:absolute;bottom:16px;right:10px;font-size:4px;font-weight:600;color:#222}
</style>
</head>
<body>

<section class="page cover" style="left:37px;top:76px">
  <div class="brand" style="left:66px;top:14px"><span class="dot" style="width:14px;height:14px"></span><span class="name" style="font-size:24px">rvtd</span><span class="tag" style="font-size:4.5px">engineering . management . construction</span></div>
  <div class="photo" role="img" aria-label="Photo of a timber-framed villa entrance among palm trees" style="left:0;top:51px;width:341px;height:163px;background:linear-gradient(180deg,#6fa6d8 0%,#8fa36a 35%,#b7692f 60%,#3f6b2c 100%)"></div>
  <p style="position:absolute;left:0;right:0;top:224px;text-align:center;font-size:4.5px;letter-spacing:2px;font-weight:600;color:#333">www.rvtdharbourline.com</p>
</section>

<section class="page welcome" style="left:441px;top:76px">
  <div class="photo" role="img" aria-label="Photo of a cliffside villa above the sea under a blue sky" style="left:0;top:0;width:239px;height:242px;background:linear-gradient(180deg,#1c4fa6 0%,#1c4fa6 20%,#6fa0dc 30%,#b9cfe8 42%,#a98a5c 58%,#7d6b48 70%,#1f5fae 74%,#2b6cc0 100%)"></div>
  <h1 style="position:absolute;left:14px;top:12px;font-family:Montserrat,sans-serif;font-weight:800;font-size:13px;color:#fff">WELCOME TO rvtd...</h1>
  <p style="position:absolute;left:14px;top:27px;font-size:8.5px;color:#fff">Professionals in building</p>
  <div class="brand light" style="left:14px;top:207px"><span class="dot" style="width:8px;height:8px"></span><span class="name" style="font-size:13px">rvtd</span><span class="tag" style="color:#cfe0f3">engineering . management . construction</span></div>
  <p style="position:absolute;left:14px;top:224px;font-size:3.8px;color:#fff">www.rvtdharbourline.com</p>
  <p class="copy" style="left:246px;top:42px;width:84px">If you are looking to build your ultimate dream home in your own piece of paradise, rvtd can not only make it a reality, but can do it in a way that is seamless and specifically tailored for you and your needs. rvtd covers all aspects of the building process, from conceptual project planning and design, through to completion and everything in between. Specialising in creating luxurious private residences throughout the Caribbean, rvtd has built an enviable portfolio of breathtaking villas and opulent homes for extremely satisfied clientele.</p>
  <span class="folio" style="bottom:14px">1</span>
</section>

<section class="page overview" style="left:822px;top:76px">
  <div class="photo" role="img" aria-label="Aerial photo of a villa with an infinity pool on a green hillside" style="left:0;top:0;width:341px;height:148px;background:linear-gradient(135deg,#3e6b2e 0%,#6e7d5a 40%,#8a8a86 55%,#49b4d6 70%,#3f6b2c 100%)"></div>
  <div class="photo" role="img" aria-label="Photo of an open living room looking out to the sea" style="left:244px;top:114px;width:84px;height:60px;border:2px solid #fff;background:linear-gradient(180deg,#b8542d 0%,#d8c7ad 45%,#74b6d8 70%,#c9b79a 100%)"></div>
  <p class="copy" style="left:14px;top:161px;width:220px;font-size:3.6px">rvtd caters to clients who are not able to be present for the duration of their project and therefore require building professionals to represent their best interests. From the beginning of the process, our services will help you understand in detail how we get to the end product with the agreed original parameters.</p>
  <p class="copy" style="left:14px;top:183px;width:220px;font-size:3.6px;color:var(--navy)">Our team consists largely of British and American personnel with support from local communities &amp; consists of Project Managers, Chartered Builders, Civil and Structural Engineers, Chartered Quantity Surveyors, Estimators and Qualified Electrical &amp; Mechanical Engineers.</p>
  <div class="brand" style="left:14px;top:212px"><span class="dot"></span><span class="name">rvtd</span><span class="tag">engineering . management . construction</span></div>
  <span class="folio">2</span>
</section>

<section class="page network" style="left:37px;top:332px">
  <div class="photo" role="img" aria-label="Photo of a stone villa with a green roof above a deep blue sea" style="left:0;top:0;width:341px;height:242px;background:linear-gradient(160deg,#a9c8e6 0%,#1d5fb2 18%,#17519e 45%,#5d7a3d 70%,#8a5a3a 85%,#3d6a2a 100%)"></div>
  <p class="copy white" style="left:204px;top:36px;width:126px;font-size:3.7px">rvtd has an unparalleled network of professional service providers available for any nature of high-end development, having partnered with a diverse range of premium project design teams, architects, engineers and specialist trade contractors. Due to these long and established relationships rvtd is able to provide clients the greatest choice of resources, mobilise at short notice and ensure superior client delivery every time.</p>
  <div class="brand light" style="left:20px;top:217px"><span class="dot"></span><span class="name">rvtd</span></div>
</section>

<section class="page inception" style="left:441px;top:344px">
  <div class="photo" role="img" aria-label="Photo of a coastline view from a terrace" style="left:77px;top:0;width:131px;height:34px;background:linear-gradient(180deg,#8db8e2 0%,#c8d8e6 60%,#5d7a4a 100%)"></div>
  <div class="photo" role="img" aria-label="Photo of a bright interior with sea windows" style="left:212px;top:0;width:129px;height:34px;background:linear-gradient(90deg,#c49a6e 0%,#e9e2d6 50%,#79b5da 100%)"></div>
  <div style="position:absolute;left:65px;top:34px;width:276px;height:36px;background:var(--sea)"></div>
  <h2 class="heading white" style="left:72px;top:47px;font-size:11px">PROJECT INCEPTION REPORT</h2>
  <div class="photo" role="img" aria-label="Photo of a lit stone villa at dusk" style="left:77px;top:74px;width:264px;height:94px;background:linear-gradient(180deg,#7b8aa0 0%,#b08a56 45%,#e1b15e 60%,#6b5a44 100%)"></div>
  <div class="photo" role="img" aria-label="Photo of a thatched beach pavilion" style="left:77px;top:172px;width:185px;height:70px;background:linear-gradient(180deg,#b78a50 0%,#d5b17a 40%,#d8e6ef 70%,#e8dcc6 100%)"></div>
  <div class="photo" role="img" aria-label="Photo of a stone water feature with plants" style="left:266px;top:172px;width:75px;height:70px;background:linear-gradient(135deg,#5d7a3a 0%,#8b6b4a 50%,#4e5b3a 100%)"></div>
  <p class="copy just" style="left:14px;top:112px;width:57px;font-size:3.7px">rvtd partner intrinsically with the design team through the design and planning phase to ensure that all parameters of the project are clearly defined, understood and adhered to giving clients comfort and peace of mind from the outset.</p>
  <div class="brand" style="left:14px;top:212px"><span class="dot"></span><span class="name">rvtd</span></div>
</section>

<section class="page review" style="left:822px;top:344px;height:244px">
  <h2 class="heading" style="left:14px;top:14px">DESIGN REVIEW</h2>
  <p class="copy" style="left:14px;top:28px;width:316px;font-size:3.7px">Upon completion of the construction documents, rvtd strategically reviews all drawings and specifications with any inefficiencies or irregularities reported to the client before this documentation is submitted to local planning authorities for building approval.</p>
  <div class="photo" role="img" aria-label="Photo of a timber and stone villa with warm lights by a pool" style="left:0;top:44px;width:341px;height:124px;background:linear-gradient(180deg,#6a8ab0 0%,#9a8466 40%,#d9a25a 60%,#7a6a58 85%,#4f83a8 100%)"></div>
  <h2 class="heading" style="left:14px;top:175px">COST PLANNING, BUDGETING &amp; VALUE ENGINEERING</h2>
  <p class="copy" style="left:14px;top:189px;width:316px;font-size:3.6px">rvtd can undertake vital cost analysis on the client's behalf and budgets are meticulously prepared based on the agreed scope of works. Upon evaluation of the budget, rvtd undertakes a value engineering exercise where alternate material selections, construction methodologies and project scheduling are adjusted to manage the ultimate cost of the project, without compromising on quality and service delivery.</p>
  <div class="brand" style="left:14px;top:215px"><span class="dot"></span><span class="name">rvtd</span><span class="tag">engineering . management . construction</span></div>
  <span class="folio" style="bottom:14px">5</span>
</section>

<section class="page construction" style="left:35px;top:612px;height:243px">
  <div class="photo" role="img" aria-label="Aerial photo of a hillside villa among palms" style="left:0;top:0;width:171px;height:243px;background:linear-gradient(180deg,#7c8a5c 0%,#5c7a3c 35%,#8a7a6a 60%,#3f6b2c 100%)"></div>
  <div style="position:absolute;left:171px;top:0;width:170px;height:243px;background:var(--indigo)"></div>
  <h2 class="heading white" style="left:179px;top:14px">CONSTRUCTION DEVELOPMENT</h2>
  <p class="copy white" style="left:179px;top:28px;width:155px;font-size:3.7px">Performing in the capacity of main building contractor or management contractor, rvtd subcontractors and suppliers are selected and awarded contracts through our highly refined, inhouse tendering process. rvtd partners with not only the leading companies in their respective industries, but just as importantly, the most competent and suitable companies for a specific project. Through this approach, rvtd proactively manages agreed costs and avoids unforeseen claims throughout the project lifecycle.</p>
  <h2 class="heading white" style="left:179px;top:100px">MATERIALS PROCUREMENT</h2>
  <p class="copy white" style="left:179px;top:114px;width:155px;font-size:3.7px">rvtd sources only the very finest quality materials at the most efficient price points to preserve the original design and add value for the client. Our highly experienced and knowledgeable logistics team will ensure carefree delivery to site in a safe and timely manner, every time.</p>
  <div class="brand light" style="left:14px;top:214px"><span class="dot"></span><span class="name">rvtd</span></div>
  <span class="folio" style="color:#fff;bottom:14px;right:14px">7</span>
</section>

<section class="page process" style="left:441px;top:612px;height:244px">
  <div class="photo" role="img" aria-label="Aerial photo of a modern white villa with a long pool" style="left:0;top:0;width:171px;height:122px;background:linear-gradient(135deg,#6d7f4e 0%,#9aa37a 35%,#e8ecef 50%,#3fb4d4 62%,#5a6e3a 100%)"></div>
  <h2 class="heading aqua" style="left:179px;top:46px">THE BUILDING PROCESS</h2>
  <p class="copy" style="left:179px;top:60px;width:152px;font-size:3.7px">rvtd methodically directs and co-ordinates the entire building process on-site with senior project management accessible and visible at all times to guarantee that all design standards, timelines and budgets are met or improved.</p>
  <div class="photo" role="img" aria-label="Photo of a bright living room with sea view windows" style="left:171px;top:122px;width:170px;height:122px;background:linear-gradient(180deg,#e9e4dc 0%,#79b6e0 35%,#4b9ad0 55%,#ddd6c9 80%,#b8aa94 100%)"></div>
  <h2 class="heading aqua" style="left:14px;top:154px">COMMISSIONING &amp; HANDOVER</h2>
  <p class="copy" style="left:14px;top:168px;width:152px;font-size:3.7px">rvtd commissions all internal finalisation checklists and procedures have been achieved to the highest standard. This includes, but is not limited to, thoroughly commissioning and testing every installation to ensure a move-in ready Caribbean dream home is proudly presented to the client at handover.</p>
  <div class="brand" style="left:14px;top:214px"><span class="dot"></span><span class="name">rvtd</span><span class="tag">engineering . management . construction</span></div>
</section>

<section class="page team" style="left:822px;top:612px;height:243px">
  <h2 class="heading" style="left:14px;top:18px">MANAGEMENT TEAM</h2>
  <div class="photo" role="img" aria-label="Portrait of Daniel, Co-Founder and Director" style="left:14px;top:55px;width:42px;height:58px;background:linear-gradient(180deg,#f2f2f2 0%,#d8cfc8 45%,#1e3f86 75%)"></div>
  <p class="copy" style="left:64px;top:54px;width:266px;font-size:3.6px">Daniel is a member of a chartered building institute and has an Engineering and Construction Management background with over fourteen years of both new build and renovation experience from sizeable, private residences to significant development projects throughout the United Kingdom and the Caribbean. Daniel has represented both contractor and client on several projects and is recognised industry wide as being able to successfully lead highly technical and complex projects to their desired outcome, whilst maintaining superior client and contractor relations and best in class service time and time again. Degree certified in Civil Engineering, Daniel is a professional builder who possesses deep and detailed knowledge in the areas of estimating, budgeting, scheduling, procurement and project management. As Co-Founder and Director, Daniel brings a holistic and dynamic perspective to the rvtd team.</p>
  <div class="photo" role="img" aria-label="Portrait of Owen, Senior Project Manager" style="left:14px;top:126px;width:42px;height:58px;background:linear-gradient(180deg,#f2f2f2 0%,#d8cfc8 45%,#1e3f86 75%)"></div>
  <p class="copy" style="left:64px;top:125px;width:266px;font-size:3.6px">Owen studied Civil Engineering at Northgate University, earning a BEng (Hons) degree, then a MSc in Construction Management from the University of Eastmoor. Upon leaving university Owen started his real education as a site engineer working for a large contractor before being head-hunted for his first overseas posting to work on the construction of the Palmera Hotel, Barbados. For several years through to 2014, Owen worked exclusively for Coral Ridge Estate, an exclusive five-star residential and golfing resort, as their Construction Project Manager, responsible for civil works and infrastructure projects across ultra-luxurious condominiums and villas. Owen joined rvtd in 2015 and is also the Senior Project Manager leading operations at Pelican Cay, recognised as an impressive leader with a proven ability to simplify complex issues with ease.</p>
  <div class="brand" style="left:14px;top:214px"><span class="dot"></span><span class="name">rvtd</span><span class="tag">engineering . management . construction</span></div>
  <span class="folio" style="bottom:14px">8</span>
</section>

<section class="page back" style="left:441px;top:882px">
  <div class="brand" style="left:16px;top:204px"><span class="dot" style="width:10px;height:10px"></span><span class="name" style="font-size:17px">rvtd</span><span class="tag">engineering . management . construction</span></div>
  <div class="copy" style="left:167px;top:206px;font-size:3.6px;color:#444">
    <svg width="5" height="5" viewBox="0 0 10 10" style="vertical-align:middle"><path d="M2 1h2l1 3-1.5 1a6 6 0 0 0 2.5 2.5L7 6l3 1v2h-1A8 8 0 0 1 1 2V1z" fill="#3aa7d7"/></svg> 123-456-789-456<br>
    <svg width="5" height="5" viewBox="0 0 10 10" style="vertical-align:middle"><path d="M2 1h2l1 3-1.5 1a6 6 0 0 0 2.5 2.5L7 6l3 1v2h-1A8 8 0 0 1 1 2V1z" fill="#3aa7d7"/></svg> 123-456-789-123
  </div>
  <div class="copy" style="left:223px;top:206px;font-size:3.6px;color:#444">
    <svg width="5" height="5" viewBox="0 0 10 10" style="vertical-align:middle"><circle cx="5" cy="5" r="4" fill="none" stroke="#3aa7d7" stroke-width="1.4"/></svg> www.rvtdharbourline.com<br>
    <svg width="5" height="5" viewBox="0 0 10 10" style="vertical-align:middle"><rect x="1" y="2" width="8" height="6" fill="none" stroke="#3aa7d7" stroke-width="1.4"/></svg> hello@rvtdharbourline.com
  </div>
  <div class="copy" style="left:284px;top:206px;font-size:3.6px;color:#444">
    <svg width="5" height="5" viewBox="0 0 10 10" style="vertical-align:middle"><path d="M5 10 1.5 5a3.5 3.5 0 1 1 7 0z" fill="#3aa7d7"/></svg> Your office address here
  </div>
  <p class="copy" style="left:0;right:0;top:225px;text-align:center;font-size:3.4px;color:#666">Copyright © rvtd Caribbean 2017. All Rights Reserved</p>
  <div style="position:absolute;left:0;bottom:0;width:341px;height:6px;background:var(--indigo)"></div>
</section>

</body>
</html>
```